The Negative Effects of Childhood Abuse

I'm a 4th year psychology student and I need a project poster to present my research in 2 days. I have attached a power point file includes the content of the poster. You will find few pictures in the PP file as well, and you can choose whatever picture that fits with your design. feel free to use any pictures you prefer other than mine. I have also included a picture of poster samples so you can get a better idea. I want to see designs that use the colour blue and white. Please make sure to use the University logo in top of the poster, you will find it in the attachments files. Size of the poster is also included. I want the font to be readable (e.g., use 2o's for the body and 80's for headlines ) however, reference list should be in a smaller size unlike the rest of the body. I'm looking for simple designs with bright colours. Please be fast as possible I need it before Aug 13th.. No need to get 10 designs 3-5 would be fine.

Thank you!
Mila

Industry/Entity Type

University

Colors
3176b5
0456a4
86acd3
fcfdfe

```html
<!DOCTYPE html>
<html lang="en">
<head>
<meta charset="utf-8">
<title>The Negative Effects Of Childhood Abuse</title>
<link rel="stylesheet" href="https://fonts.googleapis.com/css2?family=Carlito&family=Arimo:wght@400;700&display=swap">
<style>
  :root {
    --band: #55c3f2;
    --heading-box: #a9dcf6;
    --ink: #1a1a1a;
    --title-ink: #111111;
    --paper: #ffffff;
    --logo-ink: #0456a4;
    --sign-red: #c8403a;
  }
  * { box-sizing: border-box; margin: 0; padding: 0; }
  html, body { width: 1200px; height: 900px; overflow: hidden; background: var(--paper); }
  .poster { position: relative; width: 1200px; height: 900px; background: var(--paper); color: var(--ink); font-family: "Arimo", Arial, sans-serif; }

  .header-band { position: absolute; left: 22px; top: 12px; width: 1156px; height: 98px; background: var(--band); }
  .brand { position: absolute; left: 40px; top: 22px; width: 226px; height: 78px; background: var(--paper); display: flex; align-items: center; justify-content: center; gap: 10px; }
  .brand-mark { width: 20px; height: 20px; background: var(--logo-ink); }
  .brand-name { font-family: "Carlito", sans-serif; font-size: 24px; color: var(--logo-ink); line-height: 1; }
  .poster-title { position: absolute; left: 300px; top: 24px; width: 820px; text-align: center; font-family: "Carlito", sans-serif; font-weight: 400; font-size: 41px; color: var(--title-ink); }
  .poster-author { position: absolute; left: 300px; top: 76px; width: 820px; text-align: center; font-family: "Arimo", sans-serif; font-size: 21px; color: var(--title-ink); }

  .footer-band { position: absolute; left: 22px; top: 864px; width: 1156px; height: 8px; background: var(--band); }

  .column { position: absolute; top: 124px; font-size: 8.8px; line-height: 1.24; }
  .col-1 { left: 24px; width: 266px; }
  .col-2 { left: 310px; width: 292px; }
  .col-3 { left: 612px; width: 292px; }
  .col-4 { left: 910px; width: 268px; }

  .section-head { background: var(--heading-box); font-family: "Carlito", sans-serif; font-size: 21px; line-height: 1.1; padding: 2px 5px; margin: 0 0 9px; font-weight: 400; }
  .section-head.two-line { padding: 3px 5px; }
  p { margin-bottom: 8px; }
  ul { list-style: disc; padding-left: 14px; }
  ul li { margin-bottom: 11px; }
  ul.sub { padding-left: 16px; margin-top: 4px; list-style: disc; }
  ul.sub li { margin-bottom: 1px; }
  .figure { display: block; margin: 4px auto 10px; }

  .references { list-style: none; padding-left: 6px; font-size: 4.2px; line-height: 1.3; }
  .references li { margin-bottom: 5px; padding-left: 6px; text-indent: -6px; }
  .references li::before { content: "\2022  "; }
</style>
</head>
<body>
<div class="poster">
  <div class="header-band"></div>
  <div class="brand">
    <span class="brand-mark"></span>
    <span class="brand-name">Ridgeway University</span>
  </div>
  <h1 class="poster-title">The Negative Effects Of Childhood Abuse</h1>
  <div class="poster-author">Mila Al Nasser</div>

  <section class="column col-1">
    <h2 class="section-head">Abstract</h2>
    <p>Childhood abuse is a very important issue that causes a wide variety of damages on the victim's well-being (e.g., Halvers et al., 2010). Statistics shows that 69% of children are more likely to be abused by their parents or step-parents (Northland Statistics Bureau, 2011). Numerous studies have demonstrated that children exposed to domestic violence and/or child abuse are more likely to experience a wide range of adverse psychosocial and behavioral outcomes (e.g., Marlow &amp; Crane, 2013). The effects of being abused persist into adolescence (e.g., Nolan et al., 2006). The purpose of this essay is to demonstrate that childhood abuse can lead to depression and aggressiveness in the victim's adolescence years. The literature reviewed suggests that childhood abuse increases the probability of improving depression problems (depressive symptoms or clinical depression) (e.g., Gable et al., 2008; Halvers et al., 2010) as well as aggressive behaviors (e.g., Carrington-Lee et al., 2008; Millbrook et al., 2010) in adolescence. The association between childhood abuse and its negative psychological and behavioral outcomes are examined, and studies exploring depression and aggressiveness as two significant effects of children maltreatments in adolescence are discussed. Implications for future research are suggested.</p>

    <h2 class="section-head">Introduction</h2>
    <ul>
      <li>Child abuse is increasingly being recognized as a worldwide human rights issue and a public health problem that has significant impact on the victim's physical (e.g., Jarvis et al. 2010) and psychological well-being (e.g., Carrington-Lee et al., 2008; Hartwell et al., 2004).</li>
      <li>A report published by Northland Statistics Bureau (2011) specified that children are more likely to be abused by a member of their family than a stranger specifically, 69% of children aged 1 to 3 were abused more often by a parent or a step-parent.</li>
      <li>Findings suggest that girls suffer from child abuse more than boys (e.g., Arden et al., 2005) and this may be due to the higher rate of sexual abuse toward girls (e.g., Paxley &amp; Torvin, 2003).</li>
    </ul>
    <svg class="figure" width="120" height="116" role="img" aria-label="Photograph of a crying young child">
      <defs><linearGradient id="child-photo" x1="0" y1="0" x2="0" y2="1"><stop offset="0" stop-color="#d8cfc6"/><stop offset="1" stop-color="#e7c3a8"/></linearGradient></defs>
      <rect width="120" height="116" fill="url(#child-photo)"/>
    </svg>
    <ul>
      <li>Negative Effects of Child Abuse:
        <ul class="sub">
          <li>Low health-related quality of life (e.g., Jarvis et al., 2010).</li>
          <li>Physical injuries (e.g., Trask et al., 2012).</li>
          <li>Risk of cardiovascular disease (e.g., Marlow et al., 2013 ).</li>
          <li>Psychiatric disorders (e.g., Moreland et al., 2011).</li>
          <li>Negative behavioral consequences (e.g., McBride et al., 1997).</li>
        </ul>
      </li>
      <li>Research studies frequently found depression and aggression to be two major psychological and behavioural outcomes linked with child abuse during adolescence (e.g., Mason-Price et al., 2009; Moriyama et al., 2004).</li>
    </ul>
  </section>

  <section class="column col-2">
    <ul>
      <li><strong>Thesis:</strong> Children who were physically and/or psychologically abused by their parents more likely to develop depression problems (depressive symptoms or clinical depression) (e.g., Gable &amp; Abner, 2008; Hadley-Yates &amp; Devlin, 2008; Halvers et al., 2010;) as well as aggressive behaviors (e.g., Carrington-Lee et al., 2008; Millbrook et al., 2010; Vanderhoff et al., 2009) in adolescence.</li>
    </ul>
    <svg class="figure" width="140" height="114" role="img" aria-label="Line illustration of a parent shouting at a child holding a teddy bear">
      <rect width="140" height="114" fill="#f1f1f1"/>
    </svg>
    <h2 class="section-head">Key Terms</h2>
    <ul>
      <li><strong>Child abuse</strong> is defined as any act, or failure to act, by a parent or adult caregiver, which caused death, serious physical or emotional harm, sexual abuse or exploitation, or an act or failure to act which presents an imminent risk of serious harm toward children (Paxley &amp; Torvin, 2003).</li>
      <li><strong>Depression</strong> (depressive symptoms or clinical depression) including a variety of emotional, physiological, behavioral, and cognitive symptoms such as sadness, sleep disturbance, loss of energy, and hopelessness (Norwood-Hayes &amp; Radley, 2011).</li>
      <li>Developing <strong>aggressive behavior</strong> including any physical or verbal behavior intended to hurt someone (e.g., Carrington-Lee et al., 2008; Millbrook et al., 2010).</li>
    </ul>
    <h2 class="section-head two-line">Childhood Abuse and<br>Depression</h2>
    <ul>
      <li>Depression (depressive symptoms or clinical depression) was one of the most commonly reported negative psychological outcomes of childhood abuse among adolescents(e.g., Hadley-Yates et al., 2008; Jarvis et al., 2010).</li>
      <li>Parental abuse during childhood has been associated with an increased risk of depression (depressive symptoms or clinical depression) early adulthood (e.g., Galvan et. al., 2012).</li>
      <li>Children who were physically and/or psychologically abused are more likely to develop depression problems due to the negative impact of abuse on the ability to regulate emotions and to disturbances in neurobiological processes associated with child abuse (e.g., Galvan et al., 2012; Kerr et al., 2006).</li>
      <li>Another explanation was that children maltreatment is associated with increased of negative cognitive style of hopelessness which may affect victims' expectations of control and self-confidence (e.g., Lomax et al., 2009; Nolan et al., 2006).</li>
      <li>Childhood emotional abuse found to be a strong predictor of depressive symptoms in early adolescence (e.g., Gable &amp; Abner 2008; Kerr et al., 2006).</li>
    </ul>
  </section>

  <section class="column col-3">
    <ul>
      <li>Victims with a history of emotional maltreatment may be especially vulnerable to a cognitively mediated subtype of depression, hopelessness depression (HD) (e.g., Lomax et al., 2009).</li>
      <li>A study by Jarvis et al., (2010) suggested that messages communicated to a child via psychological aggression may be more important in contributing to psychological outcome than the actual occurrence of physical violence toward the child.</li>
    </ul>
    <h2 class="section-head two-line">Childhood Abuse and<br>Aggression</h2>
    <ul>
      <li>Another outcome that has been found related to the exposure to childhood abuse among adolescents is aggressiveness (e.g., Arden et al., 2005)</li>
      <li>High level of parental abuse was strongly associated with aggressive behavior in adolescents (e.g., Mott et al., 2004).</li>
      <li>Displaying aggressive behavior in adolescence may be due to the social learning theory where children who exposed to violence are more likely to learn from their parents to use aggressiveness in their own lives (e.g., Arden et al., 2005).</li>
      <li>A study conducted by Fenwick et al. (2010) suggested that in addition to the social learning theory principle, aggressive behavior was related to the inability to control emotions.</li>
      <li>Verbal aggression by the parents is just like physical aggression has a significant effect on contributing the aggressiveness among abused children during adolescent years (e.g., Mott et al., 2004; Merritt, 2011).</li>
      <li>Fenwick, Fairbank &amp; Conway (2010) suggested that emotional abuse has the most powerful relationship with both outward anger, expressed physically or verbally, and covert anger.</li>
      <li>Although the reasons for this relationship have not been made clear, it may be that the denigrating and humiliating nature of verbal aggression causes or exacerbates feelings of intense anger in children, which intensifies if the abuse is chronic in nature (e.g., Mercer et al., 2012; Millbrook et al., 2010).</li>
    </ul>
    <h2 class="section-head">Discussion</h2>
    <ul>
      <li>Experience of child abuse has been associated with detrimental psychological and behavioural effects. Specifically, victims of child abuse develop depression (symptoms or clinical) (e.g., Gable &amp; Abner, 2008; Hadley-Yates &amp; Devlin, 2008) as well as aggressive behaviors (e.g., Carrington-Lee et al., 2008; Millbrook et al., 2010) in adolescence.</li>
    </ul>
    <svg class="figure" width="92" height="90" role="img" aria-label="Photograph of a distressed child with a hand at the throat">
      <defs><linearGradient id="discussion-photo" x1="0" y1="0" x2="0" y2="1"><stop offset="0" stop-color="#d9d4cf"/><stop offset="1" stop-color="#b8aaa0"/></linearGradient></defs>
      <rect width="92" height="90" fill="url(#discussion-photo)"/>
    </svg>
  </section>

  <section class="column col-4">
    <ul>
      <li>Collective research on the relationship between child abuse and depression suggested that adolescents who were abused in childhood by their parents were more likely to be suffering from depressive symptoms or diagnosis of depression (e.g., Galvan, Bowden, Kwan, Georgiou, Dunmore, &amp; MacKinnon, 2012; Jarvis et al., 2010).</li>
      <li>Interestingly, research found that psychological abuse in specific was a powerful predictor of improving both depression and aggressiveness outcomes on victims who were abused in their childhood during adolescence (e.g., Mercer et al., 2012; Millbrook et al., 2010; Moriyama &amp; Shah, 2004).</li>
      <li>Victims of child abuse have also been found to report higher levels of aggressiveness (e.g., Carrington-Lee et al., 2008). Specifically, victims who exposure to family violence frequently has a high predisposition of approving violence as their strategies for resolving their conflicts and having high risk of displaying violent behavior themselves (e.g., Arden et al., 2005; Mercer et al., 2011).</li>
    </ul>
    <svg class="figure" width="90" height="82" role="img" aria-label="Photograph of a stop sign held over a child abuse placard">
      <defs><linearGradient id="stop-photo" x1="0" y1="0" x2="0" y2="1"><stop offset="0" stop-color="#9fb3c4"/><stop offset="0.55" stop-color="var(--sign-red)"/><stop offset="1" stop-color="#6c6c6c"/></linearGradient></defs>
      <rect width="90" height="82" fill="url(#stop-photo)"/>
    </svg>
    <h2 class="section-head">Recommendations</h2>
    <ul>
      <li>First, researchers should attempt to recruit youth victims of childhood abuse from the general population instead of clinical settings and protective service programs. This will help to generalize studies' results to the majority of adolescents who may be suffering from childhood abuse but who may not have sought professional help from clinicians.</li>
      <li>Researchers should measure the frequency and exact time of childhood abuse to provide more accurate association between childhood abuse with depression and aggression.</li>
    </ul>
    <h2 class="section-head">References</h2>
    <ul class="references">
      <li>Arden, M., Lowe, T., &amp; Pike, D. (2005). Single versus multiple maltreatment in adolescence. Journal of Youth Studies, 11, 20-32.</li>
      <li>Carrington-Lee, L., Doyle, R., &amp; Finch, S. (2008). Childhood maltreatment and relational aggression in early teens. Child Development, 79, 1736-1751.</li>
      <li>Fenwick, J., Fairbank, P., &amp; Conway, H. (2010). Child abuse and anger among emotionally maltreated youth. Journal of Clinical Psychology, 39, 25-34.</li>
      <li>Gable, E., &amp; Abner, A. (2008). Emotional abuse, verbal victimization and depressive symptoms. Cognitive Therapy and Research, 32, 161-176.</li>
      <li>Galvan, S., Bowden, K., &amp; Kwan, N. (2012). Childhood and family influences on depression and physical conditions. Journal of Psychiatric Research, 46, 1475-1482.</li>
      <li>Hadley-Yates, G., &amp; Devlin, H. (2008). Rates and psychological effects of exposure to family violence. Child Abuse &amp; Neglect, 32, 956-966.</li>
      <li>Hartwell, T., Ives, M., &amp; Quill, R. (2004). Pathways from physical childhood abuse to partner violence in young adulthood. Violence and Victims, 19, 123-136.</li>
      <li>Jarvis, W., Reyes, B., &amp; Stone, C. (2010). Associations between childhood adversity and depression in young adults. Child Abuse &amp; Neglect, 34, 833-841.</li>
      <li>Jessop, D., &amp; Kell, O. (2009). Child abuse in the context of domestic violence: prevalence and practice. Violence and Victims, 23, 221-235.</li>
      <li>Kendall, R., &amp; Tolle, F. (2012). The impact of child abuse history and anger on dating violence. Journal of Family Violence, 27, 165-176.</li>
      <li>Kerr, A., &amp; Moss, L. (2006). Longitudinal trajectories of self-esteem and depressive symptoms. Child Development, 77, 624-639.</li>
      <li>Lomax, V., Abbot, S., &amp; Ness, P. (2009). Emotional maltreatment and depression: a prospective prediction study. Depression &amp; Anxiety, 26, 174-181.</li>
      <li>McBride, R., &amp; Wynn, J. (1997). Multiple maltreatment experiences and adolescent behavior problems. Development and Psychopathology, 9, 131-149.</li>
    </ul>
  </section>

  <div class="footer-band"></div>
</div>
</body>
</html>
```